KestrelNet Business Cards

Create business cards for our exciting new software company. We provide cloud billing systems and provisioning software for campany that need monthly SaaS and Cloud Billing

Target Market(s)

Enterprise businesses, b2b, telecom carriers, software manufactures

Industry/Entity Type

Software

```html
<!DOCTYPE html>
<html lang="en">
<head>
<meta charset="utf-8">
<title>KestrelNet Business Cards</title>
<link href="https://fonts.googleapis.com/css2?family=Jost:wght@400;500;600&display=swap" rel="stylesheet">
<style>
  :root {
    --navy: #1b3354;
    --navy-mid: #2b5278;
    --steel: #4f86ad;
    --sky: #7fcde9;
    --paper: #ffffff;
    --canvas: #ffffff;
  }
  html, body {
    margin: 0;
    width: 1200px;
    height: 900px;
    overflow: hidden;
    background: var(--canvas);
    font-family: "Jost", sans-serif;
  }
  .stage {
    position: relative;
    width: 1200px;
    height: 900px;
  }
  .card {
    position: absolute;
    top: 285px;
    width: 540px;
    height: 330px;
    overflow: hidden;
  }
  .card svg.swoosh {
    position: absolute;
    inset: 0;
    width: 540px;
    height: 330px;
  }
  .card--front {
    left: 45px;
    background: linear-gradient(180deg, var(--navy) 0%, var(--navy) 35%, var(--navy-mid) 100%);
  }
  .card--back {
    left: 615px;
    background: var(--paper);
  }
  .front-name {
    position: absolute;
    left: 112px;
    top: 118px;
    margin: 0;
    color: var(--paper);
    font-weight: 500;
    font-size: 64px;
    letter-spacing: 0.5px;
    line-height: 1;
  }
  .front-tagline {
    position: absolute;
    right: 10px;
    bottom: 8px;
    margin: 0;
    color: var(--paper);
    font-size: 12px;
    letter-spacing: 2.4px;
    text-align: right;
    line-height: 1.55;
    text-transform: uppercase;
  }
  .back-brand {
    position: absolute;
    left: 24px;
    top: 40px;
  }
  .back-brand__name {
    margin: 0;
    color: var(--steel);
    font-weight: 500;
    font-size: 30px;
    line-height: 1;
  }
  .back-brand__tagline {
    margin: 3px 0 0;
    color: var(--steel);
    font-size: 6px;
    letter-spacing: 1px;
    text-transform: uppercase;
    line-height: 1.3;
  }
  .contact {
    position: absolute;
    left: 30px;
    top: 146px;
    color: var(--navy);
    font-weight: 600;
    font-size: 14px;
    line-height: 1.3;
    text-align: center;
    width: 250px;
  }
  .contact p { margin: 0; }
  .contact .phones { margin-top: 18px; }
  .person {
    position: absolute;
    right: 80px;
    top: 164px;
    color: var(--navy);
    text-align: center;
  }
  .person__name {
    margin: 0;
    font-weight: 600;
    font-size: 23px;
    line-height: 1.1;
  }
  .person__title {
    margin: 0;
    font-weight: 400;
    font-size: 19px;
    line-height: 1.1;
  }
</style>
</head>
<body>
<main class="stage">

  <section class="card card--front" aria-label="Business card front">
    <svg class="swoosh" viewBox="0 0 540 330" aria-hidden="true">
      <defs>
        <linearGradient id="front-band" x1="0" y1="0" x2="1" y2="0">
          <stop offset="0" stop-color="#4f86ad"/>
          <stop offset="0.6" stop-color="#7fcde9"/>
          <stop offset="1" stop-color="#8fd6ef"/>
        </linearGradient>
      </defs>
      <path d="M0,262 Q300,292 540,150 L540,168 Q300,300 0,280 Z" fill="#3f6f95"/>
      <path d="M0,285 Q310,300 540,168 L540,330 L0,330 Z" fill="url(#front-band)"/>
    </svg>
    <h1 class="front-name">KestrelNet</h1>
    <p class="front-tagline">Cloud billing and<br>operational support systems</p>
  </section>

  <section class="card card--back" aria-label="Business card back">
    <svg class="swoosh" viewBox="0 0 540 330" aria-hidden="true">
      <defs>
        <linearGradient id="back-fill" x1="0" y1="0" x2="1" y2="0">
          <stop offset="0" stop-color="#1b3354"/>
          <stop offset="0.45" stop-color="#4f86ad"/>
          <stop offset="0.75" stop-color="#7fcde9"/>
          <stop offset="1" stop-color="#7fcde9"/>
        </linearGradient>
      </defs>
      <path d="M0,276 Q320,300 540,170 L540,330 L0,330 Z" fill="url(#back-fill)"/>
      <path d="M0,270 Q320,290 540,160 L540,176 Q320,304 0,286 Z" fill="#1b3354"/>
      <path d="M0,286 Q320,304 540,176 L540,184 Q320,312 0,292 Z" fill="#7fcde9"/>
    </svg>
    <div class="back-brand">
      <p class="back-brand__name">KestrelNet</p>
      <p class="back-brand__tagline">Cloud billing and<br>operational support systems</p>
    </div>
    <div class="contact">
      <p>218 Harbor Crest Road, Suite 310</p>
      <p>Fairview, CA 90417</p>
      <div class="phones">
        <p>T:+44 (0) 120 555 0142</p>
        <p>F:+44 (0) 120 555 0142</p>
      </div>
    </div>
    <div class="person">
      <p class="person__name">Dana Marlowe</p>
      <p class="person__title">Title Here</p>
    </div>
  </section>

</main>
</body>
</html>
```